Flyer for longday centre (Childcare Centre)

We need a marketing flyer for our long day (Childcare) centre targeting childcare enrolments for 2016.

The name of the childcare is: Wexbury Vale Early Childhood Learning Centre
Location: will be provided later
Telephone: will be provided later
Email: will be provided later

The message of the flyer should have limited places now available for 2016. Enrol now.

Target Market(s)

Parents and Families

Industry/Entity Type

Childcare

Font styles to use
Sans Serif

Requirements
Must have
• Come and see why more and more families are switching to Wexbury Vale.
• We invite parents to come along to explore our facilities and our children's programs.
• We also run a government approved and funded Kindergarten program.
Nice to have
• Opening hours: 6am to 6:30pm Monday to Friday

```html
<!DOCTYPE html>
<html lang="en">
<head>
<meta charset="utf-8">
<title>Wexbury Vale Early Childhood Learning Centre – Enrol Now</title>
<link rel="stylesheet" href="https://fonts.googleapis.com/css2?family=Montserrat:wght@500;600;700;800;900&display=swap">
<style>
  :root {
    --white: #ffffff;
    --lavender: #f1ecf6;
    --magenta: #c92a5e;
    --crimson: #e0245e;
    --purple: #4b2c8a;
    --green: #2fa84f;
    --yellow: #f7c51d;
    --sky: #cfe9ff;
  }
  * { margin: 0; padding: 0; box-sizing: border-box; }
  html, body { width: 849px; height: 1200px; overflow: hidden; background: var(--white); }
  .flyer {
    position: relative;
    width: 849px;
    height: 1200px;
    overflow: hidden;
    background: var(--white);
    font-family: "Montserrat", sans-serif;
  }
  .backdrop { position: absolute; inset: 0; }
  .mascot-art {
    position: absolute;
    left: 290px; top: 16px;
    width: 270px; height: 215px;
    border-radius: 40px;
    background: linear-gradient(135deg, #f7d56b 0%, #f29a8a 50%, #8fc6ea 100%);
  }
  .brand-name {
    position: absolute;
    top: 248px; left: 0; width: 100%;
    text-align: center;
    color: var(--green);
    font-weight: 900;
    font-size: 52px;
    letter-spacing: 1px;
    line-height: 1;
  }
  .brand-tagline {
    position: absolute;
    top: 310px; left: 0; width: 100%;
    text-align: center;
    color: var(--green);
    font-weight: 600;
    font-size: 24px;
    letter-spacing: 1.5px;
    line-height: 1;
  }
  .offer {
    position: absolute;
    left: 30px; top: 382px;
    font-weight: 800;
    font-size: 30px;
    line-height: 1.2;
    color: var(--purple);
  }
  .offer .offer-lead { color: var(--crimson); display: block; }
  .copy {
    position: absolute;
    font-weight: 700;
    font-size: 23px;
    line-height: 1.35;
  }
  .copy-visit { top: 548px; left: 60px; width: 680px; text-align: center; color: var(--white); }
  .copy-invite { top: 634px; left: 170px; width: 660px; text-align: center; color: var(--yellow); }
  .copy-kinder { top: 718px; left: 30px; width: 470px; color: var(--sky); }
  .hours {
    position: absolute;
    left: 30px; top: 815px;
    color: var(--white);
    font-weight: 700;
    font-size: 23px;
    line-height: 1.35;
  }
  .contact {
    position: absolute;
    left: 30px; top: 965px;
    color: var(--yellow);
    font-style: normal;
    font-weight: 600;
    font-size: 15px;
    line-height: 1.5;
  }
</style>
</head>
<body>
<main class="flyer">
  <svg class="backdrop" width="849" height="1200" viewBox="0 0 849 1200" aria-hidden="true">
    <defs>
      <linearGradient id="warmPhoto" x1="0" y1="0" x2="1" y2="1">
        <stop offset="0" stop-color="#f0d6c2"/>
        <stop offset="1" stop-color="#c7a48a"/>
      </linearGradient>
      <linearGradient id="coolPhoto" x1="0" y1="0" x2="1" y2="1">
        <stop offset="0" stop-color="#d7e4ef"/>
        <stop offset="1" stop-color="#a9bfd3"/>
      </linearGradient>
    </defs>
    <path class="offer-band" d="M0 370 C 220 350, 420 365, 640 385 L640 520 L0 520 Z" fill="var(--lavender)"/>
    <path class="main-band" d="M0 505 C 200 485, 420 520, 849 490 L849 1200 L0 1200 Z" fill="var(--magenta)"/>
    <g role="img" aria-label="Photo collage of young children playing and learning at the centre">
      <circle cx="700" cy="430" r="100" fill="url(#warmPhoto)" stroke="#fff" stroke-width="8"/>
      <circle cx="800" cy="470" r="58" fill="url(#coolPhoto)" stroke="#fff" stroke-width="8"/>
    </g>
    <path role="img" aria-label="Photo of a smiling toddler playing with toys"
          d="M565 812 C 640 792, 760 788, 849 792 L849 1200 L525 1200 C 495 1060, 505 900, 565 812 Z"
          fill="url(#warmPhoto)" stroke="#fff" stroke-width="8"/>
  </svg>

  <div class="mascot-art" role="img" aria-label="Cheerful illustration of children with letters and numbers"></div>
  <h1 class="brand-name">WEXBURY VALE</h1>
  <p class="brand-tagline">EARLY CHILDHOOD LEARNING CENTRE</p>

  <p class="offer"><span class="offer-lead">LIMITED PLACES</span>NOW AVAILABLE FOR 2016<br>ENROL NOW.</p>

  <p class="copy copy-visit">Come and see why more and more families<br>are switching to Wexbury Vale.</p>
  <p class="copy copy-invite">We invite parents to come along to explore our facilities<br>and our children’s programs.</p>
  <p class="copy copy-kinder">We also run a government approved<br>and funded Kindergarten program.</p>

  <p class="hours">Opening hours:<br>6am to 6:30pm Monday to Friday</p>

  <address class="contact">
    Wexbury Vale Early Childhood Learning Centre<br>
    Location: 12 Larkspur Way, Fernhollow, VIC 3999<br>
    Telephone: (03) 9000 1234<br>
    Email: manager@wexbury-vale.com.au
  </address>
</main>
</body>
</html>
```